Harborline Local 482 promo banner / sign

We are a construction trade union, started in 1896. We are a proud Union and consider ourselves one of the most productive and badass of the trade Unions.
As Iron Workers we erect structural steel, we place reinforcing rebar in concrete, machinery moving, welding and ornamental steel installs, we are looking for banners/flags to be produced for parades and job fairs etc.
We also have a female contingent of our trade which i would like something specific to address the "Sisters" of our trade.
I have attached a lot of examples just to give you an idea of who we are/what we do, there is also a lot of content on the net.

Open to future work with a designer(s): If there are multiple designs i like we produced around 1000 shirts/hoodies a year and in excess of 6000 stickers so we are always looking for a bank of designs. i would like some professional designs and some badass designs as well, GOOD LUCK!

Target Market(s)

20-55 year old proud union workers

Industry/Entity Type

Construction

Colors

Designer to choose colors to be used in the design.

Requirements
Should not have
• swearing, nudity

```html
<!DOCTYPE html>
<html lang="en">
<head>
<meta charset="utf-8">
<title>Harborline Local 482 Banner</title>
<link rel="stylesheet" href="https://fonts.googleapis.com/css2?family=Poppins:wght@500;600&family=Questrial&display=swap">
<style>
  :root {
    --backdrop: #b9cdd0;
    --panel: #c9f6fc;
    --union-blue: #1351a0;
    --deep-navy: #0b1a33;
    --ink: #0d1c24;
    --white: #ffffff;
    --photo-dark: #1c2a44;
    --photo-mid: #3c5f8e;
    --photo-glow: #6fa8e8;
  }
  * { margin: 0; padding: 0; box-sizing: border-box; }
  html, body {
    width: 1200px;
    height: 528px;
    overflow: hidden;
    background: var(--backdrop);
  }
  .canvas {
    position: relative;
    width: 1200px;
    height: 528px;
  }
  .banner {
    position: absolute;
    left: 234px;
    top: 121px;
    width: 760px;
    height: 267px;
    background: var(--panel);
    overflow: hidden;
  }
  .banner-shapes {
    position: absolute;
    inset: 0;
    width: 760px;
    height: 267px;
  }
  .headline {
    position: absolute;
    left: 300px;
    right: 0;
    top: 58px;
    text-align: center;
    font-family: "Poppins", sans-serif;
    font-weight: 600;
    font-size: 40px;
    line-height: 1;
    color: var(--ink);
    padding-left: 20px;
  }
  .tagline {
    position: absolute;
    left: 300px;
    right: 0;
    top: 106px;
    text-align: center;
    font-family: "Questrial", sans-serif;
    font-size: 20px;
    line-height: 1;
    color: var(--ink);
    padding-left: 20px;
  }
  .union-line {
    position: absolute;
    left: 310px;
    right: 0;
    top: 168px;
    text-align: center;
    font-family: "Poppins", sans-serif;
    font-weight: 600;
    font-size: 12.5px;
    line-height: 16px;
    color: var(--ink);
    padding-left: 30px;
  }
  .web-address {
    position: absolute;
    left: 290px;
    right: 0;
    top: 228px;
    height: 39px;
    display: flex;
    align-items: center;
    justify-content: center;
    font-family: "Questrial", sans-serif;
    font-size: 14px;
    color: var(--white);
    padding-left: 20px;
  }
</style>
</head>
<body>
<div class="canvas">
  <section class="banner">
    <svg class="banner-shapes" viewBox="0 0 760 267" xmlns="http://www.w3.org/2000/svg">
      <defs>
        <radialGradient id="welder-tone" cx="0.62" cy="0.72" r="0.8">
          <stop offset="0" stop-color="var(--photo-glow)"/>
          <stop offset="0.35" stop-color="var(--photo-mid)"/>
          <stop offset="1" stop-color="var(--photo-dark)"/>
        </radialGradient>
      </defs>
      <rect class="photo-area" x="0" y="0" width="300" height="267" fill="url(#welder-tone)"
            role="img" aria-label="Photo of an ironworker in a welding mask welding steel, sparks glowing blue"/>
      <polygon class="photo-light" points="186,0 208,0 216,34 194,34" fill="#eef3f8"/>
      <polygon class="blue-stripe" points="133,0 186,0 194,34 175,34 245,239 286,267 286,267 288,267 262,267"
               fill="var(--union-blue)"/>
      <polygon class="blue-frame" points="208,0 250,0 316,228 760,228 760,267 286,267 281,239 226,34 216,34"
               fill="var(--union-blue)"/>
      <polygon class="blue-stripe-left" points="133,0 186,0 194,34 175,34 245,239 262,267 236,267"
               fill="var(--union-blue)"/>
      <polygon class="navy-stripe" points="175,34 226,34 281,239 286,267 262,267 245,239"
               fill="var(--deep-navy)"/>
    </svg>
    <h1 class="headline">Ironworkers</h1>
    <p class="tagline">Hard work never killed anyone</p>
    <p class="union-line">United Guild of Bridge, Ornamental and<br>reinforcement. Harborline Local 482. Building America</p>
    <p class="web-address">harborline482.org</p>
  </section>
</div>
</body>
</html>
```